Veteran Reserved Parking Sign 12x18

Steadfast Homefront Kin Alliance is looking to have a new Veteran Reserved Parking Sign designed. Included in the files are our current logo, the rectangle with the name on it. Also included is our Alt Square version that we will often use. There are several other signs that we kind of like as examples, not not asking for exactly like those, we want you to be creative and show us some new ideas. These are full sized parking signs, 12" wide X 18" height.

Target Market(s)

Veterans and Military Friendly Americans

Industry/Entity Type

Veteran Nonprofit

Font styles to use
Other font styles liked:
• Our logo uses the Franklin Heavy Gothic Font but you are not required to use that font in design.

Requirements
Must have
• Our logo needs to be on there and well as SHKA.ORG
Should not have
• CAN NOT Mention Brave Return Initiative or have black silhouettes similar to their logo. SHKA is NOT the same nonprofit.

```html
<!DOCTYPE html>
<html lang="en">
<head>
<meta charset="utf-8">
<title>Veteran Parking Sign – Steadfast Homefront Kin Alliance</title>
<link rel="stylesheet" href="https://fonts.googleapis.com/css2?family=Poppins:wght@600;700&family=Roboto+Slab:wght@800;900&display=swap">
<style>
  :root {
    --backdrop: #d1d3d4;
    --navy: #0d1d42;
    --white: #ffffff;
    --red: #b81c47;
    --flag-red: #d23a55;
    --flag-pale: #f1f1f4;
  }
  html, body {
    margin: 0;
    padding: 0;
    width: 1200px;
    height: 2991px;
    overflow: hidden;
    background: var(--backdrop);
  }
  .canvas {
    position: relative;
    width: 1200px;
    height: 2991px;
  }
  .parking-sign {
    position: absolute;
    left: 100px;
    top: 745px;
    width: 1000px;
    height: 1500px;
    display: block;
  }
  .sign-plate { fill: var(--navy); }
  .sign-border { fill: none; stroke: var(--white); stroke-width: 7; }
  .heading-reserved {
    font-family: "Roboto Slab", Georgia, serif;
    font-weight: 900;
    font-size: 122px;
    fill: var(--white);
  }
  .heading-veteran {
    font-family: "Poppins", Arial, sans-serif;
    font-weight: 700;
    font-size: 166px;
    fill: var(--white);
  }
  .heading-parking {
    font-family: "Poppins", Arial, sans-serif;
    font-weight: 700;
    font-size: 166px;
    fill: var(--red);
  }
  .divider { stroke: var(--red); stroke-width: 4; }
  .tagline {
    font-family: "Roboto Slab", Georgia, serif;
    font-weight: 800;
    font-size: 44px;
    fill: var(--white);
  }
  .star { fill: var(--white); }
  .org-mark-square { fill: var(--white); }
  .org-name {
    font-family: "Poppins", Arial, sans-serif;
    font-weight: 700;
    font-size: 88px;
    fill: var(--white);
  }
  .org-web {
    font-family: "Poppins", Arial, sans-serif;
    font-weight: 600;
    font-size: 23px;
    fill: var(--white);
  }
</style>
</head>
<body>
<main class="canvas">
  <svg class="parking-sign" viewBox="0 0 1000 1500" xmlns="http://www.w3.org/2000/svg">
    <defs>
      <linearGradient id="flag-tones" x1="0" y1="0" x2="1" y2="1">
        <stop offset="0" stop-color="#9aa3c0"/>
        <stop offset="0.35" stop-color="var(--flag-pale)"/>
        <stop offset="0.7" stop-color="var(--flag-red)"/>
        <stop offset="1" stop-color="#e9c9d0"/>
      </linearGradient>
      <path id="star-shape" d="M0,-1 L0.2245,-0.309 L0.9511,-0.309 L0.3633,0.118 L0.5878,0.809 L0,0.382 L-0.5878,0.809 L-0.3633,0.118 L-0.9511,-0.309 L-0.2245,-0.309 Z"/>
    </defs>

    <rect class="sign-plate" x="0" y="0" width="1000" height="1500" rx="60"/>
    <rect class="sign-border" x="39" y="39" width="922" height="1422" rx="52"/>

    <text class="heading-reserved" x="500" y="213" text-anchor="middle" textLength="764" lengthAdjust="spacingAndGlyphs">RESERVED</text>

    <text class="heading-veteran" x="500" y="592" text-anchor="middle" textLength="766" lengthAdjust="spacingAndGlyphs">VETERAN</text>
    <text class="heading-parking" x="500" y="754" text-anchor="middle" textLength="754" lengthAdjust="spacingAndGlyphs">PARKING</text>

    <line class="divider" x1="127" y1="783" x2="873" y2="783"/>

    <text class="tagline" x="500" y="868" text-anchor="middle" textLength="767" lengthAdjust="spacingAndGlyphs">THANK YOU FOR YOUR SERVICE</text>

    <g class="star-row">
      <use class="star" href="#star-shape" transform="translate(378 987) scale(24)"/>
      <use class="star" href="#star-shape" transform="translate(436 987) scale(26)"/>
      <use class="star" href="#star-shape" transform="translate(500 985) scale(32)"/>
      <use class="star" href="#star-shape" transform="translate(564 987) scale(26)"/>
      <use class="star" href="#star-shape" transform="translate(622 987) scale(24)"/>
    </g>

    <rect class="flag-art" role="img" aria-label="Waving American flag illustration" x="119" y="1230" width="393" height="142" rx="10" fill="url(#flag-tones)"/>

    <g class="org-mark">
      <rect class="org-mark-square" x="619" y="1280" width="62" height="62"/>
      <text class="org-name" x="700" y="1342" textLength="207" lengthAdjust="spacingAndGlyphs">SHKA</text>
    </g>
    <text class="org-web" x="907" y="1393" text-anchor="end">SHKA.ORG</text>
  </svg>
</main>
</body>
</html>
```